Minimalist Modern Business Card Design, open to ideas, or cleaner version of provided files, but what logo & logo colors (with some black) as shown in files, and info for back shown in files as well.

```html
<!DOCTYPE html>
<html lang="en">
<head>
<meta charset="utf-8">
<title>Northway Field Works – Business Card</title>
<link href="https://fonts.googleapis.com/css2?family=Montserrat:wght@400;500;600;700&display=swap" rel="stylesheet">
<style>
  :root {
    --backdrop: #ababab;
    --card-dark: #0c0c0c;
    --card-dark-mid: #151515;
    --card-light: #ffffff;
    --ink: #1a1a1a;
    --ink-soft: #3a3a3a;
    --muted: #7a7a7a;
    --rule: #cfcfcf;
    --mark-light: #c9c9c9;
  }
  * { margin: 0; padding: 0; box-sizing: border-box; }
  html, body {
    width: 1200px; height: 1000px; overflow: hidden;
    background: var(--backdrop);
    font-family: "Montserrat", sans-serif;
  }
  .canvas { position: relative; width: 1200px; height: 1000px; }
  .card {
    position: absolute; left: 294px; width: 613px; height: 352px;
    border-radius: 22px; overflow: hidden;
  }
  .card--front { top: 96px; background: var(--card-dark); }
  .card--back { top: 518px; background: var(--card-light); }

  .front-pattern {
    position: absolute; inset: 0;
    background: linear-gradient(100deg, #050505 0%, #121212 45%, #1b1b1b 75%, #101010 100%);
  }
  .front-brand {
    position: absolute; right: 62px; top: 234px;
    font-size: 15px; font-weight: 600; color: var(--mark-light);
    letter-spacing: 0.2px;
  }

  .brand-lockup {
    position: absolute; top: 47px; left: 0; right: 0;
    display: flex; justify-content: center; align-items: center; gap: 18px;
  }
  .brand-square { width: 42px; height: 42px; background: var(--ink); }
  .brand-name {
    font-size: 23px; font-weight: 600; line-height: 24px; color: var(--ink);
  }
  .person {
    position: absolute; top: 185px; left: 0; right: 0; text-align: center;
  }
  .person-name { font-size: 17px; font-weight: 700; color: var(--ink-soft); letter-spacing: 0.3px; }
  .person-title {
    margin-top: 3px; font-size: 9px; font-weight: 500; letter-spacing: 4.2px;
    color: var(--ink-soft); padding-left: 4px;
  }
  .divider {
    position: absolute; top: 284px; left: 43px; right: 43px;
    height: 1px; background: var(--rule);
  }
  .contact {
    position: absolute; top: 307px; left: 0; right: 0; text-align: center;
    font-size: 14px; color: var(--muted); letter-spacing: 0.2px;
  }
</style>
</head>
<body>
<div class="canvas">
  <section class="card card--front">
    <div class="front-pattern" role="img" aria-label="Repeating brand symbol pattern fading from black to dark grey"></div>
    <span class="front-brand">Northway Field Works</span>
  </section>

  <section class="card card--back">
    <div class="brand-lockup">
      <span class="brand-square"></span>
      <span class="brand-name">Northway<br>Field Works</span>
    </div>
    <div class="person">
      <p class="person-name">Name Surname</p>
      <p class="person-title">PRESIDENT</p>
    </div>
    <div class="divider"></div>
    <p class="contact">123-456-7890 | email@website.com | www.website.com</p>
  </section>
</div>
</body>
</html>
```